Healthy Supplement featuring Moringa products

Need 3 business card options for our reps to order from Printwell. Our reps will be ordering from Printwell once we upload them. Attached is our current designs to show what info needs to be on the cards. Our website is www.tqvitality.com
The business cards will be a template for our reps to order from. Most of our reps are Asian & Hispanic. Please look at our website so you can see who we are to get the look and feel what we need.
Target Market(s)
Adults 30 on up. Health oriented people.
Industry/Entity Type
Health And Wellness
Contact Information for Business Card
Name
Title
Phone
Logo
www.tqvitality.com/my/username
Font styles to use
Requirements
Must have
- Please match our website look and colors. A moringa leaf is nice, but am open to something different.
Nice to have
- Healthy looking and warm, not super cold or too modern.
Should not have
- No harsh colors please.

```html
<!DOCTYPE html>
<html lang="en">
<head>
<meta charset="utf-8">
<title>TQ Vitality — Business Card</title>
<link rel="stylesheet" href="https://fonts.googleapis.com/css2?family=Cinzel:wght@400;600&family=Lato:wght@400&display=swap">
<style>
  :root {
    --bg: #3a3a3a;
    --green-light: #95c81c;
    --green-mid: #7fb414;
    --green-deep: #5f9a0c;
    --orange: #f26a1b;
    --white: #ffffff;
  }
  * { box-sizing: border-box; margin: 0; padding: 0; }
  html, body { width: 1200px; height: 896px; overflow: hidden; }
  body {
    background: var(--bg);
    display: flex; flex-direction: column; align-items: center; justify-content: center;
    gap: 48px;
  }
  .card {
    position: relative; width: 640px; height: 366px; overflow: hidden;
    border-radius: 3px; box-shadow: 0 10px 24px rgba(0,0,0,.35);
  }
  .card-front { background: var(--white); }
  .card-back { background: radial-gradient(ellipse at 35% 25%, var(--green-light), var(--green-deep) 85%); }
  .wave { position: absolute; inset: 0; }
  .brand {
    display: flex; align-items: center; gap: 12px;
    font-family: "Cinzel", serif; font-weight: 600; letter-spacing: 3px;
  }
  .brand-dot { border-radius: 50%; flex: none; }
  .card-front .brand { position: absolute; left: 150px; top: 48px; font-size: 34px; color: var(--green-deep); }
  .card-front .brand-dot { width: 22px; height: 22px; background: var(--green-deep); }
  .contacts {
    position: absolute; left: 40px; top: 200px; color: var(--white);
    font-family: "Lato", sans-serif; font-size: 15px; line-height: 1.6;
  }
  .contacts li { list-style: none; display: flex; align-items: center; gap: 8px; }
  .contacts svg { width: 13px; height: 13px; fill: var(--white); }
  .person {
    position: absolute; right: 120px; bottom: 40px; text-align: right; color: var(--white);
    font-family: "Cinzel", serif; white-space: nowrap;
  }
  .person-name { font-size: 26px; letter-spacing: 2px; font-weight: 400; }
  .person-title { font-size: 16px; letter-spacing: 1px; margin-top: 2px; }
  .card-back .brand {
    position: absolute; left: 0; right: 0; top: 128px; justify-content: center;
    font-size: 46px; color: var(--white);
  }
  .card-back .brand-dot { width: 28px; height: 28px; background: var(--white); }
  .site-url {
    position: absolute; left: 0; right: 0; top: 230px; text-align: center;
    font-family: "Lato", sans-serif; font-size: 18px; color: var(--white); letter-spacing: .5px;
  }
</style>
</head>
<body>
  <section class="card card-front">
    <svg class="wave" viewBox="0 0 640 366" aria-hidden="true">
      <path d="M0,78 C120,160 250,200 380,216 C500,230 590,280 622,366 L0,366 Z" fill="var(--green-light)"/>
      <path d="M0,56 C120,142 250,184 385,200 C505,214 600,266 636,366" fill="none" stroke="var(--orange)" stroke-width="5"/>
      <path d="M0,44 C120,132 250,174 390,190 C515,204 615,254 652,366" fill="none" stroke="var(--green-light)" stroke-width="3"/>
    </svg>
    <div class="brand"><span class="brand-dot"></span>TQ VITALITY</div>
    <ul class="contacts">
      <li><svg viewBox="0 0 24 24"><path d="M6.6 10.8a15 15 0 0 0 6.6 6.6l2.2-2.2c.3-.3.7-.4 1-.2 1.1.4 2.3.6 3.6.6.6 0 1 .4 1 1V20c0 .6-.4 1-1 1A17 17 0 0 1 3 4c0-.6.4-1 1-1h3.5c.6 0 1 .4 1 1 0 1.3.2 2.5.6 3.6.1.3 0 .7-.2 1z"/></svg>055-987 654 321</li>
      <li><svg viewBox="0 0 24 24"><path d="M2 5h20v14H2z M2 5l10 8 10-8" fill="none" stroke="#fff" stroke-width="2"/></svg>info@sitemail.com</li>
    </ul>
    <div class="person">
      <p class="person-name">DANIEL REYES</p>
      <p class="person-title">Managing Director</p>
    </div>
  </section>

  <section class="card card-back">
    <div class="brand"><span class="brand-dot"></span>TQ VITALITY</div>
    <p class="site-url">www.tqvitality.com/my/username</p>
  </section>
</body>
</html>
```